Accounting firm needs a postcard design

We need a postcard design for our accounting office for a advertising campaign mailing we do yearly from a mail list we create. We are a full-service accounting office that has been in business for 35 years. I have attached our logo in different formats along with a document with a description of the services we provide. I have also attached my business card and the business card of our CPA. The business cards will have contact information for the postcard design. The contact email that will need to be on the postcard is contact@marlowtaxpartners.com.

```html
<!DOCTYPE html>
<html lang="en">
<head>
<meta charset="utf-8">
<title>Marlow Tax Partners – Postcard</title>
<link rel="stylesheet" href="https://fonts.googleapis.com/css2?family=Oranienbaum&family=Oswald:wght@300;400&family=Open+Sans:wdth,wght@75..100,400..800&display=swap">
<style>
:root{
  --navy:#1b4079;
  --green:#2e8627;
  --lime:#7dc242;
  --cream:#fbf4e8;
  --white:#ffffff;
  --stage:#5d5d5d;
  --text:#3a3a3a;
}
*{margin:0;padding:0;box-sizing:border-box}
html,body{width:1200px;height:1096px;overflow:hidden}
body{background:var(--stage);position:relative;font-family:"Open Sans",Arial,sans-serif}
.card{position:absolute;width:470px;height:313px;background:var(--white);overflow:hidden}
.card--front{left:99px;top:225px}
.card--back{left:615px;top:585px}
.card svg.shapes{position:absolute;inset:0}
.abs{position:absolute}

/* front */
.brand{left:0;width:206px;top:20px;text-align:center}
.brand__mark{width:42px;height:42px;border-radius:50%;background:var(--navy);margin:0 auto 10px}
.brand__name{font-family:"Open Sans",sans-serif;font-weight:700;font-size:10.5px;letter-spacing:1.4px;color:var(--navy)}
.brand__tag{font-size:5px;color:var(--navy);margin-top:2px;letter-spacing:.2px}
.headline{left:15px;top:129px;font-family:"Oranienbaum",serif;font-weight:400;font-size:28px;line-height:34px;color:var(--white);white-space:nowrap;transform:scaleX(.8);transform-origin:left top}
.contact{left:15px;color:var(--white);display:flex;align-items:center;gap:8px;white-space:nowrap}
.contact--mail{top:245px;font-family:"Oswald",sans-serif;font-weight:300;font-size:11px}
.contact--phone{top:263px;font-family:"Open Sans",sans-serif;font-stretch:75%;font-weight:700;font-size:14.5px}
.footer-text{font-family:"Oswald",sans-serif;font-weight:300;font-size:12.5px;white-space:nowrap}
.url--front{left:15px;top:291px;color:var(--navy)}
.address{color:var(--white);display:flex;align-items:center;gap:7px}
.address--front{left:229px;top:290px;font-size:11.5px}

/* back */
.section-title{left:15px;top:14px;color:var(--white);font-weight:800;font-size:11.5px;line-height:14px;letter-spacing:.2px}
.service{width:78px;color:var(--text);font-stretch:75%;font-size:6.2px;line-height:9.4px}
.service h3{color:var(--green);font-size:6.4px;font-weight:700;text-transform:uppercase;line-height:9px;margin-bottom:1px}
.icon{width:14px;height:14px}
.url--back{left:15px;top:290px;color:var(--white)}
.address--back{left:229px;top:289px;font-size:11.5px}
</style>
</head>
<body>

<section class="card card--front" aria-label="Postcard front">
  <svg class="shapes" width="470" height="313" viewBox="0 0 470 313">
    <defs>
      <linearGradient id="photoTone" x1="0" y1="0" x2="1" y2="1">
        <stop offset="0" stop-color="#f0e4d3"/>
        <stop offset=".45" stop-color="#d9b89c"/>
        <stop offset=".7" stop-color="#b99a5c"/>
        <stop offset="1" stop-color="#efe6da"/>
      </linearGradient>
    </defs>
    <rect class="photo-area" x="0" y="0" width="470" height="313" fill="url(#photoTone)" role="img" aria-label="Photo: cupped hands around a young green seedling growing from a pile of coins"/>
    <polygon points="0,0 168,0 320,156 202,287 0,287" fill="var(--white)"/>
    <polygon points="0,117 232,117 290,177 195,287 0,287" fill="var(--navy)"/>
    <rect x="0" y="287" width="470" height="26" fill="var(--cream)"/>
    <path d="M170,313 C185,300 190,287 215,287 L470,287 L470,313 Z" fill="var(--green)"/>
  </svg>

  <div class="abs brand">
    <div class="brand__mark"></div>
    <div class="brand__name">MARLOW TAX PARTNERS</div>
    <div class="brand__tag">Tax Preparation | Bookkeeping | Payroll | Entity Formation</div>
  </div>

  <h1 class="abs headline">Individualized Business<br>and Personal Accounting<br>services you can trust</h1>

  <div class="abs contact contact--mail">
    <svg width="11" height="8" viewBox="0 0 11 8"><rect x=".5" y=".5" width="10" height="7" fill="none" stroke="#fff"/><path d="M.5 .5 5.5 4.5 10.5 .5" fill="none" stroke="#fff"/></svg>
    contact@marlowtaxpartners.com
  </div>
  <div class="abs contact contact--phone">
    <svg width="10" height="10" viewBox="0 0 24 24"><path fill="#fff" d="M6.6 10.8a15 15 0 0 0 6.6 6.6l2.2-2.2c.3-.3.7-.4 1-.2 1.1.4 2.3.6 3.6.6.6 0 1 .4 1 1V20c0 .6-.4 1-1 1A17 17 0 0 1 3 4c0-.6.4-1 1-1h3.5c.6 0 1 .4 1 1 0 1.3.2 2.5.6 3.6.1.3 0 .7-.2 1z"/></svg>
    (555)014-2290
  </div>

  <div class="abs footer-text url--front">www.marlowtaxpartners.com</div>
  <div class="abs footer-text address address--front">
    <svg width="8" height="11" viewBox="0 0 8 11"><path fill="#fff" d="M4 0a4 4 0 0 0-4 4c0 3 4 7 4 7s4-4 4-7a4 4 0 0 0-4-4zm0 5.5A1.5 1.5 0 1 1 4 2.5a1.5 1.5 0 0 1 0 3z"/></svg>
    48 Harlan Ave., Suite 300 | Brookfield, TX 75010
  </div>
</section>

<section class="card card--back" aria-label="Postcard back">
  <svg class="shapes" width="470" height="313" viewBox="0 0 470 313">
    <polygon points="0,0 223,0 223,242 192,287 0,287" fill="var(--cream)"/>
    <polygon points="0,0 164,0 208,43 0,43" fill="var(--green)"/>
    <polygon points="190,19 231,19 231,61" fill="var(--lime)"/>
    <g stroke="#9a9a9a" stroke-width=".5" stroke-dasharray="2 1.5">
      <line x1="267" y1="190" x2="441" y2="190"/>
      <line x1="267" y1="208" x2="441" y2="208"/>
      <line x1="267" y1="227" x2="441" y2="227"/>
      <line x1="267" y1="245" x2="441" y2="245"/>
      <line x1="267" y1="264" x2="441" y2="264"/>
    </g>
    <rect x="0" y="287" width="470" height="26" fill="var(--green)"/>
    <path d="M0,287 L190,287 C180,295 178,313 165,313 L0,313 Z" fill="var(--navy)"/>
  </svg>

  <h2 class="abs section-title">Business and<br>Accounting services</h2>

  <svg class="abs icon" style="left:15px;top:56px" viewBox="0 0 14 14"><rect x="1" y="1" width="5" height="3" fill="var(--green)"/><rect x="8" y="1" width="5" height="3" fill="var(--green)"/><rect x="0" y="6" width="14" height="7" rx="1" fill="var(--green)"/><text x="7" y="11.6" font-size="5" fill="#fff" text-anchor="middle" font-family="Open Sans" font-weight="700">TAX</text></svg>
  <div class="abs service" style="left:35px;top:57px">
    <h3>Tax Preparation</h3>
    <p>With over 35 years of experience filing tax returns, we are experts in tax preparation. Including Personal Returns, Corporations, LLC's, Partnerships and State Franchise Tax Returns.</p>
  </div>

  <svg class="abs icon" style="left:108px;top:56px" viewBox="0 0 14 14"><path d="M2 0h7l3 3v11H2z" fill="var(--green)"/><rect x="4" y="9" width="1.5" height="3" fill="#fff"/><rect x="6.5" y="7" width="1.5" height="5" fill="#fff"/><rect x="9" y="8" width="1.5" height="4" fill="#fff"/></svg>
  <div class="abs service" style="left:125px;top:57px">
    <h3>Financial Reporting</h3>
    <p>We'll provide easy to understand financial reports that allow you and your team to manage cash flow, create budgets and make forecasting decisions. Depending on your needs, we can provide monthly, quarterly or yearly financial statements.</p>
  </div>

  <svg class="abs icon" style="left:15px;top:147px" viewBox="0 0 14 14"><rect x="3" y="0" width="9" height="14" rx="1" fill="var(--green)"/><g fill="#fff"><rect x="1.5" y="3" width="3" height="1"/><rect x="1.5" y="6" width="3" height="1"/><rect x="1.5" y="9" width="3" height="1"/></g></svg>
  <div class="abs service" style="left:35px;top:149px">
    <h3>Bookkeeping</h3>
    <p>Let us take over the day-to-day bookkeeping so you can get back to running your business. We offer assistance with LedgerLine setup and provide ongoing bookkeeping services. Including frequent journal entries, accounts payables &amp; receivables, sales tax reporting &amp; payments, account reconciliation, and more.</p>
  </div>

  <svg class="abs icon" style="left:108px;top:158px" viewBox="0 0 14 14"><circle cx="7" cy="7" r="6.5" fill="var(--green)"/><text x="7" y="10.3" font-size="9" fill="#fff" text-anchor="middle" font-family="Open Sans" font-weight="800">$</text></svg>
  <div class="abs service" style="left:125px;top:159px">
    <h3>Payroll Processing</h3>
    <p>Whether you have 5 employees or 100+, payroll can be an overwhelming and time consuming task. We offer full-service payroll processing. Including employee onboarding, printed or direct deposit checks, quarterly payroll report filing, yearly W-2/W-3 and 1099 printing and filing, and more.</p>
  </div>

  <div class="abs footer-text url--back">www.marlowtaxpartners.com</div>
  <div class="abs footer-text address address--back">
    <svg width="8" height="11" viewBox="0 0 8 11"><path fill="#fff" d="M4 0a4 4 0 0 0-4 4c0 3 4 7 4 7s4-4 4-7a4 4 0 0 0-4-4zm0 5.5A1.5 1.5 0 1 1 4 2.5a1.5 1.5 0 0 1 0 3z"/></svg>
    48 Harlan Ave., Suite 300 | Brookfield, TX 75010
  </div>
</section>

</body>
</html>
```